Flyer for teen fitness class at a physiotherapy clinic

We are a passionate Physiotherapy Clinic requiring a flyer to promote our new service a fitness class for teenagers, which is called Youth's FLX - Flexible Limber Xtra Power. The aim of the class is to prevents injuries in sports, improve sporting performance and provide safe activity for otherwise inactive teens. The aim of the flyer is to make people aware of this new service and interested in joining. Ideally the Flyer would incorporate blue colours. Our logo must be on the flier, and at least one or two of the photos provided. Our logo is provided in the attachments. Required information : Youth's FLX: Flexible Limber Xtra Power, times Mondays and Wednesdays 4 -5. Can be claimed on private health insurance. Expert advice to tailor a program to individual needs. For more information go www.rmpvq.com.au or phone 03)5871 6093.

Industry/Entity Type

Clinic

```html
<!DOCTYPE html>
<html lang="en">
<head>
<meta charset="utf-8">
<title>Youth's FLX - Flexible Limber Xtra Power</title>
<link rel="stylesheet" href="https://fonts.googleapis.com/css2?family=Anton&family=PT+Sans:wght@400;700&family=PT+Sans+Narrow:wght@700&display=swap">
<style>
  :root {
    --backdrop: #2a3050;
    --paper: #ffffff;
    --brand-blue: #4f75bf;
    --deep-blue: #1f6bbf;
    --navy: #2b3f86;
    --slate: #5b5f86;
    --sunny: #fcd672;
    --sky-top: #7fa6d6;
    --sky-bottom: #c9d9ec;
    --shadow-blue: #8a98b8;
  }
  * { box-sizing: border-box; margin: 0; padding: 0; }
  html, body { width: 1200px; height: 901px; overflow: hidden; }
  body { background: var(--backdrop); position: relative; font-family: "PT Sans", Arial, sans-serif; }

  .flyer {
    position: absolute; left: 310px; top: 41px;
    width: 581px; height: 818px;
    background: var(--paper); overflow: hidden;
  }
  .flyer__photo {
    position: absolute; left: 0; top: 0; width: 581px; height: 440px;
    background: linear-gradient(180deg, var(--sky-top) 0%, var(--sky-bottom) 100%);
  }
  .flyer__wave { position: absolute; left: 0; top: 0; width: 581px; height: 818px; }

  .flyer__title {
    position: absolute; left: 30px; top: 30px; width: 530px;
    font-family: "Anton", Impact, sans-serif; font-size: 112px; line-height: 1;
    color: var(--deep-blue); letter-spacing: 1px;
    -webkit-text-stroke: 3px var(--paper); paint-order: stroke fill;
    text-shadow: 6px 7px 0 var(--shadow-blue);
    transform: rotate(-3deg); transform-origin: left bottom; white-space: nowrap;
  }
  .flyer__tagline {
    position: absolute; left: 123px; top: 289px; width: 339px; height: 94px;
    background: var(--sunny); border-radius: 16px;
    display: flex; flex-direction: column; justify-content: center; align-items: center;
    font-weight: 700; font-size: 37px; line-height: 1.08; color: var(--brand-blue);
  }
  .flyer__pitch {
    position: absolute; left: 30px; top: 476px;
    font-weight: 700; font-size: 23px; line-height: 1.35; color: var(--slate);
  }
  .insurance-badge {
    position: absolute; left: 390px; top: 434px; width: 176px; height: 176px;
    border-radius: 50%; background: var(--brand-blue); color: var(--paper);
    display: flex; flex-direction: column; justify-content: center; align-items: center;
    text-align: center; font-size: 18px; line-height: 1.2;
  }
  .insurance-badge__rule { width: 120px; height: 2px; background: var(--paper); margin: 6px 0; }

  .schedule { position: absolute; left: 70px; top: 574px; }
  .schedule__label {
    display: flex; align-items: center; gap: 6px;
    font-size: 20px; color: var(--slate); width: 188px;
  }
  .schedule__label::after { content: ""; flex: 1; height: 1.5px; background: var(--slate); }
  .schedule__days {
    font-family: "PT Sans Narrow", Arial, sans-serif; font-weight: 700;
    font-size: 17px; color: var(--slate); margin-top: 2px;
  }
  .schedule__hours {
    position: absolute; left: 266px; top: 583px; width: 54px; height: 51px;
    background: var(--brand-blue); color: var(--paper);
    display: flex; align-items: center; justify-content: center;
    font-weight: 700; font-size: 22px;
  }

  .clinic-name {
    position: absolute; left: 33px; top: 712px;
    display: flex; align-items: center; gap: 12px;
    color: var(--navy); font-weight: 700; font-size: 26px; line-height: 1.05;
  }
  .clinic-name__dot { width: 26px; height: 26px; border-radius: 50%; background: var(--brand-blue); flex: none; }
  .clinic-name small { font-size: 19px; }

  .contact {
    position: absolute; left: 380px; top: 700px; width: 180px;
    text-align: center; font-size: 14px; line-height: 1.45; color: var(--brand-blue);
  }
  .contact__detail { color: #333; letter-spacing: 0.5px; }
  .contact__gap { margin-top: 6px; }
</style>
</head>
<body>
  <main class="flyer">
    <div class="flyer__photo" role="img" aria-label="Photo of two smiling teenagers jumping with arms raised against a blue sky"></div>

    <svg class="flyer__wave" viewBox="0 0 581 818" aria-hidden="true">
      <path d="M0,392 C170,440 400,405 581,318 L581,338 C400,425 170,462 0,418 Z" fill="var(--brand-blue)"/>
      <path d="M0,378 C170,426 400,391 581,304" fill="none" stroke="var(--paper)" stroke-width="5"/>
      <path d="M0,418 C170,462 400,425 581,338 L581,818 L0,818 Z" fill="var(--paper)"/>
    </svg>

    <h1 class="flyer__title">YOUTH'S FLX</h1>

    <div class="flyer__tagline">
      <span>Flexible Limber</span>
      <span>Xtra Power</span>
    </div>

    <p class="flyer__pitch">Expert advice to tailor a<br>program to individual needs</p>

    <div class="insurance-badge">
      <span class="insurance-badge__rule"></span>
      <span>Can be claimed<br>on private health<br>insurance</span>
      <span class="insurance-badge__rule"></span>
    </div>

    <div class="schedule">
      <div class="schedule__label">– Times</div>
      <div class="schedule__days">MONDAYS AND WEDNESDAYS</div>
    </div>
    <div class="schedule__hours">4-5</div>

    <div class="clinic-name">
      <span class="clinic-name__dot"></span>
      <span>Harbour Point<br><small>Sports Treatment Clinic</small></span>
    </div>

    <div class="contact">
      <div>For more information visit:</div>
      <div class="contact__detail">www.rmpvq.com.au</div>
      <div class="contact__gap">or Phone:</div>
      <div class="contact__detail">(03)5871 6093</div>
    </div>
  </main>
</body>
</html>
```